TRV Law Firm Business Card & Stationary Set
Dorvenko Law Office
Use same font as used in my logo
Good Times
Simple
Marla J. Dorvenko, Esq.
3862 E. Pellham Avenue
Suite 217
Cedar Hollow, OH 60913
mjd@trvcounsel.example
www.trvcounsel.example
My colors are blue and grey
Blue values are as follows:
R: 23, G: 21, and B: 104 OR C: 100, M:92, Y:0, and K:20
Grey values are as follows:
C:0, M:0, Y:0, and K:70
Good Times is my font - let's see how it looks for all the type, but if it's too much, we will use other, modern fonts for all the information on the business cards and stationary. I prefer a fonts like Century Gothic and Calibri- nothing with serifs
I will upload the source files, but here are the guidelines. You may deviate somewhat from this.
BUSINESS CARD:
Two sided card. Back side options:
1. All blue background with logo/icon and domain address
2. Plain (white) background with logo/icon from design #476 and domain address
3. Something else
STATIONARY:
Letterhead should NOT contain any watermarks in the middle of the sheet. Letterhead should only be designed at the top and bottom (if your design requires it).
For both business cards and stationary, please be aware of the following:
For digital printing, thin borders are expensive to print with any type of consistency. I see a lot of these types of designs on ZQ. Please use these sparingly. I will probably ask you to revise them. If you cannot fit a row of small type text in your border, it is too small.
This is the main logo I want used for the front of the business card and for the letterhead and envelopes.
If you choose to, the logo/icon ONLY portion of this design may be used on the back of the business card.
If you choose to, you may reverse out the logo/icon ONLY in the blue values I provided on the back of the business card.

```html
<!DOCTYPE html>
<html lang="en">
<head>
<meta charset="utf-8">
<title>Dorvenko Law Office – Business Card</title>
<link href="https://fonts.googleapis.com/css2?family=Michroma&family=Questrial&display=swap" rel="stylesheet">
<style>
  :root{
    --brand-blue:#171568;
    --brand-blue-mid:#2f3a9e;
    --brand-grey:#6d6e71;
    --soft-grey:#e9eaee;
    --card-white:#ffffff;
    --backdrop:#d9dade;
  }
  *{margin:0;padding:0;box-sizing:border-box}
  html,body{width:1200px;height:901px;overflow:hidden}
  body{background:var(--backdrop);font-family:"Questrial",sans-serif;color:var(--brand-grey)}
  .canvas{width:1200px;height:901px;display:flex;flex-direction:column;align-items:center;justify-content:center;gap:36px}
  .card{position:relative;width:720px;height:411px;background:var(--card-white);border-radius:14px;overflow:hidden;box-shadow:0 6px 18px rgba(0,0,0,.18)}

  /* back side */
  .card-back{display:flex;flex-direction:column;align-items:center;justify-content:center;gap:26px}
  .back-mark{display:flex;align-items:center;gap:22px}
  .mark-dot{width:86px;height:86px;border-radius:50%;background:var(--brand-blue)}
  .back-name{font-family:"Michroma",sans-serif;font-size:30px;color:var(--brand-blue);letter-spacing:2px}
  .back-web{font-size:17px;letter-spacing:4px;color:var(--brand-grey)}

  /* front side */
  .side-band{position:absolute;left:0;top:0;width:84px;height:100%;background:linear-gradient(180deg,var(--brand-blue-mid),var(--brand-blue))}
  .front-dot{position:absolute;left:44px;top:30px;width:80px;height:80px;border-radius:50%;background:var(--brand-grey);border:6px solid var(--card-white)}
  .faint-circle{position:absolute;right:-70px;bottom:-90px;width:330px;height:330px;border-radius:50%;background:var(--soft-grey);opacity:.8}
  .wordmark{position:absolute;left:150px;top:40px;font-family:"Michroma",sans-serif;color:var(--brand-blue);font-weight:400}
  .wordmark .firm{display:block;font-size:46px;letter-spacing:1px;line-height:1.1}
  .wordmark .office{display:block;font-size:24px;letter-spacing:3px;text-align:right;margin-top:4px;line-height:1.1}
  .rule{position:absolute;left:150px;top:140px;width:215px;height:2px;background:var(--brand-grey)}
  .details{position:absolute;left:330px;top:170px;font-size:13.5px;line-height:1.45}
  .details .person{color:var(--brand-blue);font-size:16px;margin-bottom:8px}
  .contact{position:absolute;left:170px;top:264px;padding-left:12px;border-left:1px solid var(--brand-grey);font-size:13.5px;line-height:1.5}
  .contact b{color:var(--brand-blue);font-weight:400;display:inline-block;width:16px}
  .contact .web{color:var(--brand-blue);margin-top:4px}
</style>
</head>
<body>
<main class="canvas">
  <section class="card card-back" aria-label="Business card back">
    <div class="back-mark">
      <span class="mark-dot"></span>
      <span class="back-name">DORVENKO</span>
    </div>
    <p class="back-web">www.trvcounsel.example</p>
  </section>

  <section class="card card-front" aria-label="Business card front">
    <div class="side-band"></div>
    <span class="front-dot"></span>
    <div class="faint-circle"></div>
    <h1 class="wordmark"><span class="firm">DORVENKO</span><span class="office">LAW OFFICE</span></h1>
    <div class="rule"></div>
    <div class="details">
      <p class="person">Marla J. Dorvenko, Esq.</p>
      <p>3862 E. Pellham Avenue</p>
      <p>Suite 217</p>
      <p>Cedar Hollow, OH 60913</p>
    </div>
    <div class="contact">
      <p><b>P</b>(847) 555-0148</p>
      <p><b>F</b>(847) 555-0192</p>
      <p><b>C</b>(312) 555-0176</p>
      <p><b>E</b>mjd@trvcounsel.example</p>
      <p class="web">www.trvcounsel.example</p>
    </div>
  </section>
</main>
</body>
</html>
```